Foot and ankle surgeon requires a website design

I need a website where prospective and established patients can obtain information and then direct them to making appointments. My practice is a highly professional surgical practice specialising in surgery to the foot and ankle. My title is Mr Colin Dwyer, Podiatric Foot & Ankle Surgeon. My qualifications are: BSc MSc FACPS
The practice website will require information on: Locations, phone numbers to make appointments, general background on podiatric surgery,
I would like to include information on: my hospital appointments, surgical fellowships held, training programs undertaken, association memberships, publications written, links to useful websites
A page dedicated to common foot conditions would be useful and also a page with referral information including an online registration section that will be sent direct to the receptionist.
Examples of similar websites include:
http://www.trevorkeplinfeet.com.au/
http://www.vollardfootsurgeon.com.au/
I will provide files on logo, self photos and my personal training history etc.
Also if there is going to be a background theme I personally am associated with surfing and beach activities, it would be great if this was able to be reflected in the design.
Thank you.

```html
<!DOCTYPE html>
<html lang="en">
<head>
<meta charset="utf-8">
<title>Mr Colin Dwyer – Podiatric Foot &amp; Ankle Surgeon</title>
<link href="https://fonts.googleapis.com/css2?family=Lato:wght@400;700;900&display=swap" rel="stylesheet">
<style>
  :root {
    --orange: #f77414;
    --navy: #1d2f6b;
    --nav-grey: #6e6e6e;
    --body-grey: #8a8a8a;
    --sand: #ebeae6;
    --sand-dark: #dcdad4;
    --white: #ffffff;
  }
  * { margin: 0; padding: 0; box-sizing: border-box; }
  html, body { width: 1200px; height: 1000px; overflow: hidden; }
  body {
    position: relative;
    background: var(--white);
    font-family: 'Lato', Arial, sans-serif;
  }
  .sand-strip {
    position: absolute; left: 0; top: 0; width: 1200px; height: 25px;
    background: linear-gradient(180deg, var(--sand), var(--sand-dark));
  }
  .site-header {
    position: absolute; left: 0; top: 25px; width: 1200px; height: 162px;
    background: var(--white);
  }
  .brand {
    position: absolute; left: 104px; top: 66px;
    display: flex; align-items: center; gap: 14px;
  }
  .brand-mark {
    width: 34px; height: 34px; border-radius: 50%;
    border: 3px solid var(--navy);
  }
  .brand-name {
    font-size: 27px; font-weight: 700; color: var(--navy);
  }
  .main-nav {
    position: absolute; left: 399px; top: 35px; height: 107px;
    display: flex; align-items: center;
  }
  .nav-item {
    font-size: 15px; font-weight: 700; color: var(--nav-grey);
    text-transform: uppercase; margin-right: 22px; letter-spacing: -0.2px;
  }
  .nav-item.is-active {
    background: var(--orange); color: var(--white);
    height: 107px; width: 61px; display: flex; align-items: center;
    justify-content: center; margin-right: 12px;
  }
  .hero-band {
    position: absolute; left: 0; top: 187px; width: 1200px; height: 588px;
    background:
      repeating-linear-gradient(170deg, rgba(0,0,0,0.03) 0 40px, rgba(255,255,255,0.05) 40px 110px),
      linear-gradient(180deg, #e9e8e4, #efeeea);
  }
  .hero-image {
    position: absolute; left: 97px; top: 60px; width: 960px; height: 472px;
    background:
      linear-gradient(160deg, #f4a21a 0%, #f5c15a 30%, #f8dc9a 48%, #e7a21c 60%, #e59a12 100%);
    box-shadow: 0 18px 24px -12px rgba(0,0,0,0.35);
  }
  .intro-bar {
    position: absolute; left: 0; top: 803px; width: 1200px; height: 62px;
  }
  .intro-title {
    position: absolute; left: 97px; top: 16px;
    color: var(--orange); font-size: 22px; font-weight: 700;
  }
  .intro-title .credentials { font-size: 17px; font-weight: 400; }
  .intro-divider {
    position: absolute; left: 659px; top: 0; width: 3px; height: 62px;
    background: var(--orange);
  }
  .cta-button {
    position: absolute; left: 780px; top: 8px; width: 277px; height: 47px;
    background: var(--orange); color: var(--white);
    font-size: 19px; font-weight: 900; text-transform: uppercase;
    display: flex; align-items: center; justify-content: center;
    letter-spacing: -0.3px;
  }
  .about-section {
    position: absolute; left: 89px; top: 919px; width: 480px;
  }
  .about-heading {
    font-size: 19px; font-weight: 700; color: var(--navy);
    text-transform: uppercase; margin-bottom: 20px;
  }
  .about-text {
    font-size: 17px; font-weight: 700; color: var(--body-grey); line-height: 24px;
  }
  .about-media {
    position: absolute; left: 660px; top: 918px; width: 405px; height: 82px;
    background: radial-gradient(ellipse at 78% 90%, #3f6fae 0%, #16243f 25%, #000 50%);
  }
</style>
</head>
<body>
  <div class="sand-strip"></div>

  <header class="site-header">
    <div class="brand">
      <span class="brand-mark"></span>
      <span class="brand-name">Mr Colin Dwyer</span>
    </div>
    <nav class="main-nav">
      <span class="nav-item is-active">Home</span>
      <span class="nav-item">Mr Colin Dwyer</span>
      <span class="nav-item">Common Conditions</span>
      <span class="nav-item">Podiatric Surgery</span>
      <span class="nav-item">Contact Us</span>
    </nav>
  </header>

  <section class="hero-band">
    <div class="hero-image" role="img" aria-label="Golden sunlit beach with a wave washing over the sand and a trail of footprints"></div>
  </section>

  <section class="intro-bar">
    <h1 class="intro-title">Mr Colin Dwyer - <span class="credentials">BSc MSc FACPS | Podiatric Surgeon</span></h1>
    <div class="intro-divider"></div>
    <a class="cta-button">Find Out More</a>
  </section>

  <section class="about-section">
    <h2 class="about-heading">About Foot Surgery</h2>
    <p class="about-text">Lorem ipsum dolor sit amet, vix ad eleifend iudicabit assentior, probatus pericula constituto eos id. Reque dicit</p>
  </section>

  <div class="about-media" role="img" aria-label="X-ray image of foot bones in blue on a black background"></div>
</body>
</html>
```